Stainless Steel Water Bottle Packaging

We need a design for our cylindrical water bottle packaging.

Please see attached template (500ml cola bottle template .ai file) for exact dimensions.

VORO is defined as the elemental forces of nature embodied in an object or person. The design should be eye catching and draw potential clients in. Although its a cylindrical bottle/box, the front which would face the customer when sitting on a shelf should clearly display our logo.

Industry/Entity Type

Steel

Requirements
Must have
• Designed to the specifications of the attached template (see attached)
• Our VORO Logo (see attached) and website www.vorobottle.example(in smaller font) must appear.
• Size of bottle must appear - '17 oz/500 ml'
• These should appear somewhere:
• 'INULATED DOUBLE-WALL STAINLESS STEEL WATER BOTTLE'
• 'VORO Bottles magically keeps drinks cold for up to 24hrs, hot for 12',
• 'BPA Free'
• 'For every VORO bottle purchased, a portion of proceeds will go towards charity. Each of our colour's have been assigned a specific charity. Please visit www.vorobottle.example to find out which charity you helped support!'
• The Top circle - just our Symbol (flame/drop)
• The bottom circle - 'Inc. Designed in Canada made in China' on the outer edge leaving the middle empty for the UPC code.
• Reference website for the bottle case I'm looking for:
• http://shopkorinday.example/t-flow-lagoon-pink-insulated-water-bottle
Nice to have
• illustration of our water bottle shape (see attached) appearing somewhere on the box is something i had in mind but definitely not necessary.

```html
<!DOCTYPE html>
<html lang="en">
<head>
<meta charset="utf-8">
<title>VORO Bottle Tube Packaging</title>
<link rel="stylesheet" href="https://fonts.googleapis.com/css2?family=Montserrat:wght@400;500;600;700&display=swap">
<style>
  :root {
    --stage: #000000;
    --cream: #f6f1e6;
    --cream-deep: #ece4d2;
    --blue: #1a86c2;
    --blue-light: #7cc3e6;
    --blue-deep: #0e6ea8;
    --orange: #f2a01e;
    --orange-light: #f7c35a;
    --orange-deep: #e68a12;
    --ink: #1d1d1d;
    --logo-blue: #1678ad;
    --green: #3e9a3a;
    --badge-blue: #1a4f9c;
    --badge-orange: #e0661c;
    --bottle-light: #ecebe6;
    --bottle-shade: #d9d8d2;
  }
  * { box-sizing: border-box; margin: 0; padding: 0; }
  html, body {
    width: 1200px; height: 1200px; overflow: hidden;
    background: var(--stage);
    font-family: "Montserrat", sans-serif;
  }
  .canvas { position: relative; width: 1200px; height: 1200px; }

  .tube {
    position: absolute; top: 68px; width: 272px; height: 892px;
    border-radius: 30px; overflow: hidden;
  }
  .tube--left { left: 96px; }
  .tube--front { left: 464px; }
  .tube--right { left: 854px; }

  .tube__top {
    position: absolute; left: 0; top: 0; width: 100%; height: 64px;
    background: var(--cream-deep);
    display: flex; align-items: center; justify-content: center;
  }
  .tube__top-mark {
    width: 36px; height: 36px; border-radius: 50%; background: var(--logo-blue);
  }

  /* side panel */
  .side__wash {
    position: absolute; left: 0; top: 64px; width: 100%; height: 828px; display: flex;
  }
  .side__wash-blue {
    width: 52%;
    background: linear-gradient(180deg, var(--blue-light) 0%, var(--blue) 40%, var(--blue-deep) 70%, var(--blue-light) 100%);
  }
  .side__wash-orange {
    width: 48%;
    background: linear-gradient(180deg, var(--orange-light) 0%, var(--orange) 45%, var(--orange-deep) 75%, var(--orange-light) 100%);
  }
  .side__note {
    position: absolute; top: 296px; height: 536px;
    background: rgba(255,255,255,0.28); border-radius: 6px;
    writing-mode: vertical-rl; transform: rotate(180deg);
    display: flex; align-items: flex-start; justify-content: center;
    padding: 12px 8px;
    font-size: 12px; line-height: 1.3; color: var(--ink); font-weight: 500;
  }
  .side__note--charity { left: 52px; width: 62px; font-style: italic; }
  .side__note--visit { left: 154px; width: 56px; }
  .side__note strong { font-weight: 700; }

  /* front panel */
  .front__body { position: absolute; left: 0; top: 64px; width: 100%; height: 828px; background: var(--cream); }
  .front__wash {
    position: absolute; left: 0; top: 230px; width: 100%; height: 580px;
    background:
      radial-gradient(ellipse 45% 55% at 8% 50%, var(--orange) 0%, rgba(242,160,30,0.55) 55%, rgba(242,160,30,0) 100%),
      radial-gradient(ellipse 45% 55% at 95% 55%, var(--blue) 0%, rgba(26,134,194,0.55) 55%, rgba(26,134,194,0) 100%);
  }
  .front__logo {
    position: absolute; left: 0; top: 140px; width: 100%;
    display: flex; align-items: center; justify-content: center; gap: 10px;
  }
  .front__logo-dot { width: 22px; height: 22px; border-radius: 50%; background: var(--orange); }
  .front__logo-name {
    font-size: 58px; font-weight: 500; color: var(--logo-blue); letter-spacing: 2px; line-height: 1;
  }
  .front__web {
    position: absolute; left: 0; top: 238px; width: 100%; text-align: center;
    font-size: 14px; font-weight: 500; color: var(--ink); letter-spacing: 0.5px;
  }
  .front__product {
    position: absolute; left: 0; top: 262px; width: 100%; text-align: center;
    font-size: 8.5px; font-weight: 600; color: var(--ink); line-height: 1.3; letter-spacing: 0.6px;
  }
  .front__tagline {
    position: absolute; left: 0; top: 294px; width: 100%; text-align: center;
    font-size: 13.5px; font-weight: 500; color: var(--ink); line-height: 1.3; letter-spacing: 0.3px;
  }
  .front__bottle-area {
    position: absolute; left: 68px; top: 364px; width: 124px; height: 436px;
    border-radius: 40px 40px 16px 16px;
    background: linear-gradient(90deg, var(--bottle-shade) 0%, var(--bottle-light) 40%, var(--bottle-light) 70%, var(--bottle-shade) 100%);
  }
  .badge {
    position: absolute; left: 104px; width: 54px; height: 54px; border-radius: 50%;
    display: flex; flex-direction: column; align-items: center; justify-content: center;
    font-size: 12px; line-height: 1.05; text-align: center;
  }
  .badge strong { font-weight: 700; font-size: 13px; }
  .badge--bpa { top: 588px; background: #fff; border: 2px solid var(--green); color: var(--green); font-weight: 700; }
  .badge--cold { top: 656px; background: var(--badge-blue); color: #fff; }
  .badge--hot { top: 724px; background: var(--badge-orange); color: #fff; }
  .front__size {
    position: absolute; left: 0; top: 824px; width: 100%; text-align: center;
    font-size: 12px; font-weight: 500; color: var(--ink);
  }

  .base-disc { position: absolute; left: 494px; top: 976px; width: 200px; height: 200px; }
  .base-disc__text { font-family: "Montserrat", sans-serif; font-size: 11.5px; font-weight: 500; fill: var(--ink); }
</style>
</head>
<body>
<main class="canvas">

  <section class="tube tube--left" aria-label="Side panel">
    <div class="tube__top"><span class="tube__top-mark"></span></div>
    <div class="side__wash" role="img" aria-label="Blue and orange watercolour wash">
      <div class="side__wash-blue"></div><div class="side__wash-orange"></div>
    </div>
    <p class="side__note side__note--charity">For every VORO bottle purchased, a portion of proceeds will go towards charity. Each of our colour's have been assigned a specific charity.</p>
    <p class="side__note side__note--visit"><span>Please visit <strong>www.vorobottle.example</strong> to find out which charity you helped support!</span></p>
  </section>

  <section class="tube tube--front" aria-label="Front panel">
    <div class="tube__top"><span class="tube__top-mark"></span></div>
    <div class="front__body"></div>
    <div class="front__wash" role="img" aria-label="Orange and blue watercolour splashes"></div>
    <div class="front__logo"><span class="front__logo-dot"></span><span class="front__logo-name">VORO</span></div>
    <p class="front__web">www.vorobottle.example</p>
    <p class="front__product">INSULATED DOUBLE-WALL<br>STAINLESS STEEL WATER BOTTLE</p>
    <p class="front__tagline">VORO Bottles Magically Keeps Drinks<br>cold for up to 24hrs, hot for 12</p>
    <div class="front__bottle-area" role="img" aria-label="Illustration of the VORO water bottle shape"></div>
    <div class="badge badge--bpa"><span>BPA</span><span>FREE</span></div>
    <div class="badge badge--cold"><strong>COLD</strong><span>24hrs</span></div>
    <div class="badge badge--hot"><strong>HOT</strong><span>12hrs</span></div>
    <p class="front__size">17 oz/500 ml</p>
  </section>

  <section class="tube tube--right" aria-label="Side panel">
    <div class="tube__top"><span class="tube__top-mark"></span></div>
    <div class="side__wash" role="img" aria-label="Blue and orange watercolour wash">
      <div class="side__wash-blue"></div><div class="side__wash-orange"></div>
    </div>
    <p class="side__note side__note--charity">For every VORO bottle purchased, a portion of proceeds will go towards charity. Each of our colour's have been assigned a specific charity.</p>
    <p class="side__note side__note--visit"><span>Please visit <strong>www.vorobottle.example</strong> to find out which charity you helped support!</span></p>
  </section>

  <svg class="base-disc" viewBox="0 0 200 200" aria-label="Bottom circle">
    <defs>
      <path id="arc-top" d="M18 100 A82 82 0 0 1 182 100"/>
      <path id="arc-bottom" d="M18 100 A82 82 0 0 0 182 100"/>
    </defs>
    <circle cx="100" cy="100" r="99" fill="#fbf6e8"/>
    <text class="base-disc__text"><textPath href="#arc-top" startOffset="50%" text-anchor="middle">Inc. Designed in Canada made in China</textPath></text>
    <text class="base-disc__text"><textPath href="#arc-bottom" startOffset="50%" text-anchor="middle" dominant-baseline="hanging">Inc. Designed in Canada made in China</textPath></text>
    <circle cx="32" cy="100" r="6" fill="var(--ink)"/>
    <circle cx="168" cy="100" r="6" fill="var(--ink)"/>
    <text x="12" y="104" class="base-disc__text">★</text>
    <text x="178" y="104" class="base-disc__text">★</text>
  </svg>

</main>
</body>
</html>
```